First of a series of workplace posters- our values statement

To produce a high quality poster of our values, we would like one in a3 and one in a4 both full colour
By utilising the supplied text , the intent is to produce a really striking poster for all our work places, which set out our company values. we are looking for really strong graphical elements which support the message visually . This will be the first of a series of posters, so we are looking to establish at stylistic theme for all with this one. for more on our business,

Target Market(s)

Internal and external audiences, our clients are all tier one companies

Requirements
Must have
• contemporary design rather than conservative, visually striking
• Must be clearly readable from a reasonable distance
Nice to have
• would be nice to tie in to the blue and greens of our logo in similar fashion to our website. www.kbtgreenworks.com
Should not have
• Difficult to read fonts,

```html
<!DOCTYPE html>
<html lang="en">
<head>
<meta charset="utf-8">
<title>Our Values – KBT Greenworks</title>
<link href="https://fonts.googleapis.com/css2?family=Montserrat:wght@400;500;600;700&family=Heebo:wght@300;400;500;700&display=swap" rel="stylesheet">
<style>
:root{
  --navy:#0d2c72;
  --lime:#a3e43a;
  --green:#6cb300;
  --charcoal:#4a4a4c;
  --white:#ffffff;
  --ink:#2b2b2b;
}
*{margin:0;padding:0;box-sizing:border-box}
html,body{width:912px;height:1200px;overflow:hidden;background:var(--white)}
.poster{position:relative;width:912px;height:1200px;overflow:hidden;background:var(--white);font-family:"Montserrat",sans-serif;color:var(--ink)}
.corner-band{position:absolute;left:0;top:0}
.hero{position:absolute;left:0;top:0}
.brand{position:absolute;left:0;width:912px;top:46px;display:flex;justify-content:center;align-items:center;gap:10px}
.brand-dot{width:26px;height:26px;border-radius:50%;background:var(--green)}
.brand-name{font-family:"Montserrat",sans-serif;font-weight:700;font-size:30px;color:var(--navy);letter-spacing:.5px}
.hero-title{position:absolute;left:0;width:912px;top:282px;text-align:center;font-weight:600;font-size:60px;line-height:1;color:var(--lime);letter-spacing:-1px}
.hero-lede{position:absolute;left:90px;width:732px;top:352px;text-align:center;font-family:"Heebo",sans-serif;font-weight:300;font-size:15.5px;line-height:21px;color:var(--white)}
.col-right{position:absolute;left:439px;top:408px;width:473px;height:792px;background:var(--navy)}
.pill{position:absolute;display:flex;align-items:center;font-weight:700;border-radius:0 34px 34px 0}
.pill--navy{background:var(--navy);color:var(--white)}
.pill--green{background:var(--green);color:var(--white)}
.pill--lime{background:var(--lime);color:var(--navy)}
.sub{position:absolute;font-weight:700}
.ticks{position:absolute;list-style:none}
.ticks li{position:relative;padding-left:26px}
.ticks li::before{content:"";position:absolute;left:0;top:2px;width:11px;height:11px;border:1.5px solid currentColor;border-radius:50%}
.ticks li::after{content:"";position:absolute;left:4px;top:1px;width:5px;height:9px;border-right:2px solid currentColor;border-bottom:2px solid currentColor;transform:rotate(40deg)}
.ticks--green li::before,.ticks--green li::after{border-color:var(--green)}
.ticks--white li::before,.ticks--white li::after{border-color:var(--white)}
.ticks--navy li::before,.ticks--navy li::after{border-color:var(--navy)}
.ticks--left{left:34px;width:390px;font-size:12.5px;line-height:16.5px;color:#333}
.ticks--left li{margin-bottom:0}
.ticks--right{left:462px;width:420px;color:var(--white);font-size:12.5px;line-height:16px}
.ticks--right li{margin-bottom:1px}
.body-copy{position:absolute;font-family:"Heebo",sans-serif;font-weight:400}
.note{position:absolute;left:60px;font-size:12.5px;color:#333}
.succeed{position:absolute;left:0;top:1079px;width:460px;height:110px;background:var(--charcoal);padding:12px 20px 0 30px;color:var(--white)}
.succeed h2{font-weight:700;font-size:28px;letter-spacing:-.3px;line-height:1}
.succeed p{font-family:"Heebo",sans-serif;font-weight:300;font-size:12.5px;line-height:15px;margin-top:9px}
.together{position:absolute;left:431px;top:1079px;width:481px;height:110px;background:var(--lime);border-radius:44px 0 0 44px;padding:9px 20px 0 36px;color:var(--navy);font-family:"Heebo",sans-serif}
.together h3{font-size:12.5px;font-weight:700;margin-bottom:3px;padding-left:0}
.together .ticks{position:static;font-size:12px;line-height:15px}
.together .ticks li{margin-bottom:2px}
.footer-strip{position:absolute;left:0;top:1189px;width:912px;height:11px}
.footer-strip .l{position:absolute;left:0;top:0;width:439px;height:11px;background:var(--white)}
.footer-strip .r{position:absolute;left:439px;top:0;width:473px;height:11px;background:var(--navy)}
</style>
</head>
<body>
<main class="poster">
  <svg class="corner-band" width="912" height="60" viewBox="0 0 912 60" aria-hidden="true">
    <polygon points="640,0 912,0 912,60 580,60" fill="#0d2c72"/>
  </svg>

  <svg class="hero" width="912" height="410" viewBox="0 0 912 410">
    <defs>
      <linearGradient id="heroTone" x1="0" y1="0" x2="1" y2="0.4">
        <stop offset="0" stop-color="#7d8a92"/>
        <stop offset="0.35" stop-color="#2c3444"/>
        <stop offset="0.55" stop-color="#c9a48e"/>
        <stop offset="0.7" stop-color="#1d2638"/>
        <stop offset="1" stop-color="#c7ccd2"/>
      </linearGradient>
      <clipPath id="heroClip">
        <path d="M58 33 H225 L441 178 L678 33 H854 Q882 33 882 61 V380 Q882 408 854 408 H58 Q30 408 30 380 V61 Q30 33 58 33 Z"/>
      </clipPath>
    </defs>
    <g clip-path="url(#heroClip)">
      <rect x="0" y="0" width="912" height="410" fill="url(#heroTone)" role="img" aria-label="Photo of two business people in suits shaking hands over a desk"/>
      <rect x="0" y="265" width="912" height="145" fill="#3a3a3c" opacity="0.9"/>
    </g>
  </svg>

  <div class="brand">
    <span class="brand-dot"></span>
    <span class="brand-name">KBT Greenworks</span>
  </div>

  <h1 class="hero-title">OUR VALUES</h1>
  <p class="hero-lede">These are the key things we value, we measure all our daily activities against these. They define the way we do business.</p>

  <div class="col-right"></div>

  <!-- Left column -->
  <div class="pill pill--navy" style="left:0;top:431px;width:372px;height:60px;padding-left:34px;font-size:19px;line-height:21px">We value our people above<br>everything else</div>
  <div class="sub" style="left:34px;top:505px;font-size:18px;color:var(--green)">We demonstrate this by:</div>
  <ul class="ticks ticks--green ticks--left" style="top:538px">
    <li>Providing safe, positive, enjoyable workplaces where everyone feels valued and respected.</li>
    <li>Providing careers, not jobs, we grow together.</li>
    <li>Encouraging inclusion, participation and collaboration.</li>
    <li>Recognising and rewarding contribution and excellence.</li>
    <li>Supporting our people through tough times.</li>
    <li>Fostering healthy work life balance.</li>
  </ul>

  <div class="pill pill--green" style="left:0;top:714px;width:372px;height:61px;padding-left:34px;font-size:19px;line-height:21px">All our workplaces are<br>safe work places</div>
  <p class="body-copy" style="left:34px;top:786px;width:400px;font-size:11.5px;line-height:14.5px;color:#333;font-weight:300">There is nothing more important to us than our team members going home healthy and safe every day, we won’t accept anything less. We believe workplace safety is a management choice, by providing safe work systems and education we achieve our daily goal of Zero Harm.</p>
  <ul class="ticks ticks--green ticks--left" style="top:872px">
    <li>Take the time to make our work areas safe, whatever it takes.</li>
    <li>Don’t accept shortcuts.</li>
    <li>Look out for each other.</li>
    <li>Investigate our incidents and learn from them, no repeats.</li>
    <li>Are constantly looking for ways to improve the safety of our workplaces and the health of our team members.</li>
  </ul>
  <p class="note" style="top:1036px">Think safe, work safe, go home safe!</p>

  <!-- Right column -->
  <div class="pill pill--lime" style="left:439px;top:431px;width:356px;height:60px;padding-left:23px;font-size:19px">We are proud of who we are</div>
  <div class="sub" style="left:462px;top:505px;font-size:19px;line-height:22px;color:var(--white)">Our reputation means the<br>world to us. We:</div>
  <ul class="ticks ticks--white ticks--right" style="top:563px">
    <li>Treat everyone with respect, and we expect it in return.</li>
    <li>Follow the rules.</li>
    <li>Do what we say we will do.</li>
    <li>Own our mistakes and we fix them.</li>
    <li>Are trustworthy and transparent.</li>
  </ul>

  <div class="pill pill--lime" style="left:439px;top:686px;width:358px;height:59px;padding-left:26px;font-size:19px;line-height:21px">The planet benefits from<br>our existence</div>
  <p class="body-copy" style="left:486px;top:753px;width:300px;font-size:11px;line-height:14px;color:var(--white);font-weight:300">We are relentlessly pursuing our objective of providing our clients with pathways to sustainable development. To achieve our vision we</p>
  <ul class="ticks ticks--white ticks--right" style="top:805px;width:290px">
    <li>Minimise our environmental impact in everything we do.</li>
    <li>Actively develop and promote world’s best practices in rehabilitation of disturbed land.</li>
  </ul>

  <div class="pill pill--lime" style="left:439px;top:903px;width:296px;height:49px;padding-left:34px;font-size:19px">We set the standard</div>
  <ul class="ticks ticks--white ticks--right" style="top:975px;width:440px;font-family:'Heebo',sans-serif;font-weight:300;font-size:12.5px">
    <li style="margin-bottom:12px">We are uncompromising on quality.</li>
    <li style="margin-bottom:12px">We are the best at what we do, and we do what we are best at.</li>
    <li>We are always improving</li>
  </ul>

  <!-- Bottom band -->
  <section class="succeed">
    <h2>WE SUCCEED TOGETHER</h2>
    <p>We believe in win-win relationships. When our Business is profitable everyone benefits, our shareholders, employees, clients, suppliers and the community.</p>
  </section>
  <section class="together">
    <h3>AT KBT We:</h3>
    <ul class="ticks ticks--navy">
      <li>Work as a team, we get it done together</li>
      <li>Are building on our success and growing together</li>
      <li>Choose to work with employees, customers, and suppliers who fit our values.</li>
    </ul>
  </section>

  <div class="footer-strip"><span class="l"></span><span class="r"></span></div>
</main>
</body>
</html>
```